Various Designs

We need various designs for our new hand disinfectant dispensers that feature three extra-large windows that allow users to customize the appearance simply by changing the graphics.
Each dispenser has one window at the front and one on each side. The front window can have two different sizes. Please refer to attached zip file named Dispenser_Design_Templates.
The designs should be fresh and of high quality. Please don't just place a photo and spam me.
The design should also contain our logo (Brunvale Helvetia - is included in the template).
The design should further be professional enough for a medical and public setting. The dispensers will be used in hospitals, medical facilities, old pension homes, schools, restaurants, kitchens, public places etc.
We value creativity a lot!
It would be great if the dispenser features a slogan such as "Hand Hygiene Saves Lives". I have added a number of slogans at the end of this description.
Do not use dark colors such as brown. These colors do not stand for hygiene. You can use black but only in conjunction with a bright color.
The following files contain designs that I like:
- 01w
- velmixdecor
- worldwide
- IMG_0137
Slogans:
- Hand Hygiene Saves Lives
- Did you wash your hands?
- Did you disinfect your hands?
- Protect Yourself and Your Patients
- Healthy Hands Start Here
- Hand Hygiene We Love... We Care... We Share...
- Clean hands prevent germs from spreading.
- Practice Good Hand Hygiene
- Save Lives: Clean Your Hands
- Save Lives: Disinfect Your Hands
- Washing Hands Saves Lives
- Wash Your Hands Please
- Be aware…..!!!!! Wash with care…..!!!!!
- Hand Hygiene Station
- Hand Hygiene Share your care, not your germs
- Good Hand Hygiene It's Critical Sanitize Wash Moisturize
- Disinfect (image of a hand)
- Clean (image of a hand)
- No Water? No Problem. Waterless Hand Rub. Keep it Handy.
- Wash your hands! If not for yourself, then do it for them.
- Practice good hygiene - it-s contagious!
- Be aware, wash with care!
- Filthy fingers forecast sickness and sadness.
- Hand Hygiene The power is in your hands
- Bury the germ, Wash your hands
- Sanitize your hands and support our clean hands initiative
- Sanitize your hands. Together we can make a difference.
- You are grand if you wash your hand.
- Holding hands feels better when they’re clean.
- Be wise wash hands often.
- Wash those germs away!!!
- Your Hands Can Be Dangerous. Disinfect them to keep germs away.
- Ten out of ten patients prefer care from clean hands.
- Safety first, disinfect and protect
- It’s universal- handwashing every patient every time!
- Infection control is in your hands.
- Make your intention prevention. Wash your hands

```html
<!DOCTYPE html>
<html lang="en">
<head>
<meta charset="utf-8">
<title>Hand Hygiene Saves Lives – Dispenser Window</title>
<link href="https://fonts.googleapis.com/css2?family=Oswald:wght@400;500;600&display=swap" rel="stylesheet">
<style>
  :root {
    --leaf-deep: #4f8a12;
    --leaf-mid: #8cc43a;
    --leaf-light: #c8e46e;
    --glow: #f4fbd2;
    --grass: #5fa51c;
    --grass-dark: #3c7410;
    --text-white: #ffffff;
    --logo-blue: #1f3f8f;
    --logo-panel: #ffffff;
  }
  * { margin: 0; padding: 0; box-sizing: border-box; }
  html, body {
    width: 736px;
    height: 1200px;
    overflow: hidden;
    background: #ffffff;
  }
  .window-artwork {
    position: relative;
    width: 736px;
    height: 1200px;
    overflow: hidden;
    background:
      radial-gradient(ellipse 60% 30% at 50% 62%, rgba(255,255,255,0.25), transparent 70%),
      linear-gradient(180deg, var(--leaf-mid) 0%, var(--leaf-light) 22%, #a9d24d 50%, #95c63c 75%, #86bc30 100%);
  }
  .foliage {
    position: absolute;
    top: 0; left: 0;
    width: 100%;
    height: 330px;
    background:
      radial-gradient(circle at 52% 38%, var(--glow) 0%, rgba(244,251,210,0.7) 12%, transparent 32%),
      radial-gradient(ellipse 45% 55% at 15% 20%, var(--leaf-deep), transparent 70%),
      radial-gradient(ellipse 40% 50% at 88% 15%, var(--leaf-deep), transparent 70%),
      linear-gradient(180deg, rgba(79,138,18,0.7), rgba(140,196,58,0));
  }
  .grass {
    position: absolute;
    bottom: 0; left: 0;
    width: 100%;
    height: 170px;
    background: linear-gradient(180deg, rgba(95,165,28,0) 0%, var(--grass) 40%, var(--grass-dark) 100%);
  }
  .brand-panel {
    position: absolute;
    top: 362px;
    left: 104px;
    width: 528px;
    height: 80px;
    background: var(--logo-panel);
    display: flex;
    align-items: center;
    justify-content: center;
    gap: 16px;
    box-shadow: 0 3px 8px rgba(0,0,0,0.18);
  }
  .brand-mark {
    width: 22px;
    height: 22px;
    background: var(--logo-blue);
  }
  .brand-name {
    font-family: 'Oswald', sans-serif;
    font-weight: 500;
    font-size: 40px;
    color: var(--logo-blue);
    letter-spacing: 1px;
  }
  .slogan {
    position: absolute;
    top: 520px;
    left: 0;
    width: 100%;
    text-align: center;
    font-family: 'Oswald', sans-serif;
    color: var(--text-white);
    text-transform: uppercase;
    text-shadow: 0 4px 10px rgba(30,60,0,0.35);
  }
  .slogan-lead {
    display: block;
    font-weight: 500;
    font-size: 66px;
    line-height: 1;
    letter-spacing: 1px;
  }
  .slogan-main {
    display: block;
    font-weight: 500;
    font-size: 168px;
    line-height: 0.98;
    letter-spacing: 2px;
  }
</style>
</head>
<body>
  <main class="window-artwork">
    <div class="foliage" role="img" aria-label="Sunlit green leaves against a bright sky"></div>
    <div class="grass" role="img" aria-label="Fresh green grass along the bottom edge"></div>

    <div class="brand-panel">
      <span class="brand-mark"></span>
      <span class="brand-name">Brunvale Helvetia</span>
    </div>

    <h1 class="slogan">
      <span class="slogan-lead">Hand Hygiene</span>
      <span class="slogan-main">Saves</span>
      <span class="slogan-main">Lives</span>
    </h1>
  </main>
</body>
</html>
```